Loyalty Program

I would like to have a flyer designed to promote and explain our loyalty program targeting the local customers purchasing stationery, which then a percentage goes to the local schools in the form of Craft Products for the school children to use in their projects.
Thought of calling it :" Paper Pals" but open to other ideas
Regards
Derek

Target Market(s)

The idea is to have parents of the children at schools purchase more stationery locally, which will then give more craft and stationery resources for the children to use at school. To save parents and teachers the extra expense of buying extra school supplies during the year.

Industry/Entity Type

School

Requirements
Must have
• . Community focus
. Helping the children learn and develop creative skills
. Simple one page flyer

```html
<!DOCTYPE html>
<html lang="en">
<head>
<meta charset="utf-8">
<title>Paper Pals Loyalty Program</title>
<link rel="stylesheet" href="https://fonts.googleapis.com/css2?family=Caudex:wght@700&family=Chewy&family=Fira+Sans:wght@400;500;700&family=PT+Sans+Narrow&family=Playfair+Display:wght@700&display=swap">
<style>
  :root {
    --cream: #efe6d2;
    --sky: #8fb4d4;
    --sky-light: #b8d0e4;
    --sage: #bcd49e;
    --tan: #dcc9a3;
    --purple: #4a4a8e;
    --red: #d62e2e;
    --sun: #f6d33a;
    --blue-head: #5b8fc2;
    --ink: #1e1e1e;
    --white: #ffffff;
    --agency-green: #1f6b3a;
  }
  * { margin: 0; padding: 0; box-sizing: border-box; }
  html, body { width: 928px; height: 1200px; overflow: hidden; background: var(--cream); }
  .flyer { position: relative; width: 928px; height: 1200px; overflow: hidden; background: var(--cream); }
  .backdrop { position: absolute; inset: 0; }

  .photo { position: absolute; box-shadow: 4px 5px 10px rgba(0,0,0,.35); }
  .photo-classroom-bg { left: 0; top: 0; width: 400px; height: 534px; box-shadow: none; opacity: .55;
    background: linear-gradient(160deg, #d9c4ad 0%, #c8b59f 40%, #e6ddcd 100%); }
  .photo-girls { left: 323px; top: 260px; width: 574px; height: 381px;
    background: linear-gradient(135deg, #b59a76 0%, #e4c9a6 35%, #a9744f 60%, #3f5f9a 100%); }
  .photo-boys { left: 27px; top: 594px; width: 590px; height: 391px;
    background: linear-gradient(120deg, #c85b3a 0%, #e0b98f 30%, #7a4a30 55%, #5b83c2 80%, #d9d0c0 100%); }

  .headline { position: absolute; font-family: "Caudex", Georgia, serif; font-weight: 700; color: var(--purple); line-height: 1; }
  .headline-buying { left: 44px; top: 40px; font-size: 92px; }
  .headline-local { left: 116px; top: 164px; font-size: 92px; }
  .tagline { position: absolute; left: 88px; top: 262px; font-family: "Caudex", Georgia, serif; font-weight: 700;
    font-size: 50px; line-height: 57px; color: var(--purple); }

  .program-name { position: absolute; left: 420px; top: 76px; width: 470px; text-align: center;
    font-family: "Chewy", cursive; font-size: 96px; font-weight: 400;
    color: var(--red); line-height: 1; letter-spacing: 2px;
    text-shadow: 3px 3px 0 var(--sun), -2px -2px 0 var(--sun), 2px -2px 0 var(--sun), -2px 2px 0 var(--sun); }
  .program-sub { position: absolute; left: 420px; top: 200px; width: 470px; text-align: center;
    font-family: "Playfair Display", Georgia, serif;
    font-weight: 700; font-size: 28px; letter-spacing: 5px; color: var(--ink); }

  .info-card { position: absolute; left: 560px; top: 654px; width: 328px; height: 304px; }
  .info-card svg { position: absolute; left: -6px; top: -6px; width: 340px; height: 316px; }
  .info-body { position: relative; padding: 16px 20px 0; text-align: center; }
  .info-title { font-family: "Fira Sans", Arial, sans-serif; font-weight: 400; font-size: 23px; color: var(--blue-head); }
  .info-text { font-family: "PT Sans Narrow", Arial, sans-serif; font-size: 12.6px; line-height: 17px; color: var(--ink); margin-top: 3px; }
  .info-text strong { font-weight: 700; }
  .info-highlight { font-family: "Fira Sans", Arial, sans-serif; font-weight: 400; font-size: 27px; line-height: 31px; color: var(--red); margin-top: 8px; }
  .info-highlight + .info-text { margin-top: 4px; }

  .agency { position: absolute; left: 601px; top: 1008px; width: 247px; height: 154px; background: var(--white);
    padding: 40px 14px 0 40px; }
  .agency-name { font-family: "Fira Sans", Arial, sans-serif; font-weight: 700; font-size: 22px; line-height: 24px;
    color: var(--agency-green); }
  .agency-contact { font-family: "PT Sans Narrow", Arial, sans-serif; font-size: 11px; line-height: 13px; color: var(--ink);
    margin-top: 10px; text-align: right; }
</style>
</head>
<body>
<main class="flyer">
  <svg class="backdrop" width="928" height="1200" viewBox="0 0 928 1200" aria-hidden="true">
    <rect width="928" height="1200" fill="var(--cream)"/>
    <polygon points="400,0 607,0 607,262 400,262" fill="var(--sky)"/>
    <polygon points="607,0 928,0 928,255 607,255" fill="var(--white)"/>
    <polygon points="880,0 928,0 928,560 880,540" fill="var(--sky-light)"/>
    <polygon points="0,500 330,470 330,640 0,620" fill="var(--sage)"/>
    <polygon points="0,640 30,640 30,1000 0,1000" fill="var(--tan)"/>
    <polygon points="600,640 928,600 928,760 620,800" fill="var(--sage)"/>
    <polygon points="0,1000 300,990 240,1200 0,1200" fill="var(--sky)"/>
    <polygon points="300,1060 520,985 600,1200 340,1200" fill="var(--sage)"/>
    <polygon points="560,990 928,960 928,1200 610,1200" fill="var(--sky)"/>
    <polygon points="250,1020 300,1020 300,1110 250,1110" fill="var(--tan)"/>
  </svg>

  <div class="photo photo-classroom-bg" role="img" aria-label="Faded photo of children drawing in a classroom"></div>

  <h1 class="headline headline-buying">Buying</h1>
  <div class="headline headline-local">Local</div>
  <p class="tagline">Helps<br>your kids<br>learn &amp;<br>develop<br>creative<br>skills!</p>

  <h2 class="program-name">Paper Pals</h2>
  <p class="program-sub">Loyalty Program</p>

  <div class="photo photo-girls" role="img" aria-label="Photo of two young girls drawing with crayons at a classroom table"></div>
  <div class="photo photo-boys" role="img" aria-label="Photo of two young boys colouring at a classroom table"></div>

  <section class="info-card">
    <svg viewBox="-6 -6 340 316" aria-hidden="true">
      <path fill="var(--white)" stroke="var(--red)" stroke-width="2" d="M0,0
        h328 v304 h-328 Z"
        stroke-dasharray="6 3"/>
    </svg>
    <div class="info-body">
      <h3 class="info-title">Community involvement.</h3>
      <p class="info-text">Purchasing locally helps to reduce costs for parents which will give more craft and stationery resources to your local schools for the children to use at school.</p>
      <h3 class="info-highlight">A percentage of your purchase goes to local schools!</h3>
      <p class="info-text">Our <strong>“Paper Pals Loyalty Program”</strong> saves parents and teachers the extra expense of buying additional school supplies during the year. With your help, kids have the resources needed to bring out their creative side.</p>
    </div>
  </section>

  <aside class="agency">
    <p class="agency-name">MAPLEWOOD<br>NEWS AGENCY</p>
    <p class="agency-contact">Shop 4 / 112 Elm Rd, Maplewood 4120<br>Ph: 07 3555 0142<br>email: maplewood_news@example.com.au</p>
  </aside>
</main>
</body>
</html>
```